New Business Card Design*

We are a recruitment company based in Norwich/Cambridge England.
I have included our company logo which we want to remain the same.

What we are looking for is a new creative Business card which will really stand out!!

Contact Information for Business Card

Harriet Vance
email: Harriet@brelvix.co.uk
Address: Tolworth House
Ashgrove Innovation Park
Pelham Road
Norwich
KT9 3QD
Tel:01632 960418

```html
<!DOCTYPE html>
<html lang="en">
<head>
<meta charset="utf-8">
<title>Brelvix Business Card</title>
<link rel="stylesheet" href="https://fonts.googleapis.com/css2?family=Arimo:wght@400;700&display=swap">
<style>
  :root {
    --page: #d2d2d4;
    --card-grey: #8a868b;
    --accent-green: #9dbf3b;
    --stripe-light: #e4e4e4;
    --paper: #ffffff;
    --ink-grey: #7f7b80;
  }
  * { box-sizing: border-box; margin: 0; padding: 0; }
  html, body {
    width: 1200px; height: 990px; overflow: hidden;
    background: var(--page);
    font-family: "Arimo", Arial, sans-serif;
  }
  .card {
    position: absolute; left: 220px;
    width: 760px; height: 424px;
    border-radius: 22px; overflow: hidden;
    box-shadow: 0 4px 10px rgba(0,0,0,0.18);
  }
  .card--front { top: 41px; background: var(--paper); }
  .card--back { top: 525px; background: var(--card-grey); }
  .card__waves { position: absolute; inset: 0; width: 100%; height: 100%; }

  .holder { position: absolute; left: 50px; top: 84px; }
  .holder__name { color: var(--accent-green); font-weight: 700; font-size: 23px; letter-spacing: 0.2px; }
  .holder__role { color: var(--ink-grey); font-size: 19px; margin-top: 2px; }

  .brand { position: absolute; display: flex; flex-direction: column; }
  .brand__row { display: flex; align-items: center; gap: 12px; }
  .brand__dot { width: 44px; height: 44px; border-radius: 50%; background: var(--accent-green); }
  .brand__name { font-weight: 700; line-height: 1; }
  .brand__tagline { font-size: 10px; letter-spacing: 4.2px; margin-top: 6px; }

  .card--front .brand { left: 370px; top: 64px; }
  .card--front .brand__name { font-size: 56px; color: var(--ink-grey); }
  .card--front .brand__tagline { color: var(--ink-grey); padding-left: 56px; }

  .card--back .brand { left: 56px; top: 66px; }
  .card--back .brand__name { font-size: 72px; color: var(--paper); }
  .card--back .brand__tagline { color: var(--paper); font-size: 13px; letter-spacing: 5.4px; }

  .contact { position: absolute; left: 50px; top: 296px; list-style: none; color: var(--paper); font-size: 19px; }
  .contact li { display: flex; align-items: center; gap: 10px; height: 26px; }
  .contact svg { width: 16px; height: 16px; flex: none; }

  .address { position: absolute; right: 52px; top: 322px; text-align: right; color: var(--paper); font-size: 19px; line-height: 26px; font-style: normal; }

  .website { position: absolute; left: 56px; bottom: 46px; color: var(--paper); font-size: 20px; }
  .website__domain { color: var(--accent-green); }
</style>
</head>
<body>

<section class="card card--front" aria-label="Card front">
  <svg class="card__waves" viewBox="0 0 474 264" preserveAspectRatio="none" aria-hidden="true">
    <path d="M0,146 C120,126 230,120 320,138 C400,154 440,162 474,162 L474,176 C440,176 400,168 320,150 C230,132 120,140 0,158Z" fill="var(--stripe-light)"/>
    <path d="M0,138 C120,118 230,112 320,130 C400,146 440,150 474,148 L474,162 C440,162 400,158 320,142 C230,124 120,128 0,148Z" fill="var(--accent-green)"/>
    <path d="M0,156 C120,138 230,130 320,148 C400,166 440,174 474,176 L474,264 L0,264Z" fill="var(--card-grey)"/>
  </svg>

  <div class="holder">
    <p class="holder__name">HARRIET VANCE</p>
    <p class="holder__role">General Manager</p>
  </div>

  <div class="brand">
    <div class="brand__row">
      <span class="brand__dot"></span>
      <span class="brand__name">Brelvix</span>
    </div>
    <span class="brand__tagline">Technology Recruitment</span>
  </div>

  <ul class="contact">
    <li>
      <svg viewBox="0 0 16 16"><path d="M4 1.5 L6.5 4.5 L5 6.5 C6 8.5 7.5 10 9.5 11 L11.5 9.5 L14.5 12 L12.5 14.5 C7 14 2 9 1.5 3.5Z" fill="var(--accent-green)"/></svg>
      01632 960418
    </li>
    <li>
      <svg viewBox="0 0 16 16"><rect x="1.5" y="3.5" width="13" height="9" fill="none" stroke="var(--accent-green)" stroke-width="1.6"/><path d="M1.5 3.5 L8 9 L14.5 3.5" fill="none" stroke="var(--accent-green)" stroke-width="1.6"/></svg>
      Harriet@brelvix.co.uk
    </li>
    <li>
      <svg viewBox="0 0 16 16"><circle cx="8" cy="8" r="6.5" fill="none" stroke="var(--accent-green)" stroke-width="1.4"/><ellipse cx="8" cy="8" rx="2.8" ry="6.5" fill="none" stroke="var(--accent-green)" stroke-width="1.2"/><path d="M1.5 8 H14.5" stroke="var(--accent-green)" stroke-width="1.2"/></svg>
      www.brelvix.co.uk
    </li>
  </ul>

  <address class="address">
    Tolworth House, Pelham Road<br>
    Norwich KT9 3QD
  </address>
</section>

<section class="card card--back" aria-label="Card back">
  <div class="brand">
    <div class="brand__row">
      <span class="brand__name">Brelvix</span>
    </div>
    <span class="brand__tagline">Technology Recruitment</span>
  </div>

  <p class="website">www.<span class="website__domain">brelvix</span>.co.uk</p>
</section>

</body>
</html>
```